web page template design

We'd like to see a few designs based on the selected logo. See attached color logo.

We'll need a homepage design which will display the competition announcement and limited details about it. There will be links (or tabs) to the follow on pages which will contain all of the legal details, sign-up and design submission page, finalist selection page, winner announcement page, jury (judges) background page, company sponsor (Marlowe) details, press release page and a blog page. These are just guidelines for the number of subpage links.

So we'd like a primary page and a follow-on page which is a little more plain.

Here is the competition briefer below:

In January 2014, Marlowe Tile Inc. will launch its 1st Annual Marlowe Tile Floor Design Competition. This design competition will be open to Design and Architecture students of the NYC area. Students and student groups can submit cork flooring design concepts online to a judging committee of prominent designers and architects who will select design finalists and a winner. The winning design will highlight the unique creative possibilities of sustainable cork tiles. The winner will receive a cash prize and publication of their winning design through press releases and various media outlets as well as on the TileVexa.example website. The winning floor will be created and photographed by Marlowe Tile and will be donated to a deserving non-profit community center in NYC. The donated cork floor will be installed at no cost to the non-profit community center.

Target Market(s)

designers and architects.

Industry/Entity Type

Non-Profit

Requirements
Must have
• tabs or link system

```html
<!DOCTYPE html>
<html lang="en">
<head>
<meta charset="utf-8">
<title>Marlowe Tile Floor Design Competition 2014</title>
<link rel="stylesheet" href="https://fonts.googleapis.com/css2?family=Open+Sans:wght@300;400;600;700&family=Ubuntu:wght@400;500&display=swap">
<style>
:root{
  --red:#b8312f;--mustard:#c98d1c;--yellow:#f2c34a;--khaki:#d6d08c;--teal:#5aa3b2;
  --paper:#f7f9f9;--ink:#333;--muted:#9a9a9a;--line:#d9dcdc;
  --footer:#0e0e0e;--footer-base:#1c1c1c;--link:#e05a4a;--tw:#4aa7d6;
}
*{margin:0;padding:0;box-sizing:border-box}
html,body{width:1108px;height:1200px;overflow:hidden;background:#fff}
body{font-family:"Open Sans",sans-serif;color:var(--ink)}
.page{position:absolute;left:0;top:0;width:1200px;height:1300px;transform:scale(.92333);transform-origin:0 0}
.abs{position:absolute}
.stripe{position:absolute;left:80px;width:1040px;display:flex}
.stripe span{flex:none;height:100%}
.stripe .s1{width:182px;background:var(--red)}.stripe .s2{width:219px;background:var(--mustard)}
.stripe .s3{width:220px;background:var(--yellow)}.stripe .s4{width:218px;background:var(--khaki)}
.stripe .s5{width:201px;background:var(--teal)}
.header{left:80px;top:0;width:1040px;height:158px;background:var(--paper)}
.brand{left:524px;top:27px;width:152px;height:101px;background:#f1f3f3;text-align:center}
.brand .dot{width:44px;height:44px;border-radius:50%;background:var(--mustard);margin:5px auto 8px}
.brand .name{font-family:"Ubuntu",sans-serif;font-weight:500;font-size:12px;color:#4a2a1a;letter-spacing:.3px}
.nav{top:135px;left:285px;display:flex;gap:18px;font-size:8.5px;font-weight:600;letter-spacing:.5px;color:#555}
.auth{top:135px;left:809px;font-size:8.5px;font-weight:700;letter-spacing:.5px;color:var(--red)}
.auth b{margin:0 11px;font-weight:400}
.hero{left:80px;top:158px;width:1040px;height:351px;background:linear-gradient(100deg,#6a4a3a 0%,#8b6a58 30%,#a5826c 55%,#9a7b66 75%,#b79d8a 100%)}
.badge{left:293px;top:219px;width:107px;height:20px;background:var(--teal);color:#fff;font-size:8px;font-weight:700;line-height:20px;padding-left:23px}
.badge svg{position:absolute;left:9px;top:6px}
.hero-title{left:287px;top:250px;font-weight:300;font-size:40px;line-height:47px;color:var(--yellow);width:560px}
.hero-text{left:291px;top:358px;width:500px;font-size:12.2px;line-height:16.3px;color:#fff}
.btn{left:292px;top:430px;width:92px;height:37px;border:1px solid #fff;color:#fff;font-size:8.5px;font-weight:700;text-align:center;line-height:35px;letter-spacing:.3px}
.main{left:80px;top:509px;width:1040px;height:504px;background:var(--paper)}
.sec-title{font-family:"Ubuntu",sans-serif;font-size:15px;color:#3a3a3a;display:flex;align-items:center;gap:6px}
.rule{height:1px;background:var(--line)}
.card{left:294px;top:585px;width:400px;height:161px;background:#fff}
.card h3{position:absolute;left:0;top:3px;width:150px;font-family:"Ubuntu",sans-serif;font-weight:400;font-size:15px;line-height:19.5px;color:#2e2e2e}
.time{font-size:8.5px;color:#aaa}
.card p{position:absolute;left:0;top:97px;width:150px;font-size:8.5px;line-height:15.5px;color:#555}
.card p a{color:var(--link);text-decoration:none}
.img-city{left:156px;top:0;width:244px;height:161px;background:linear-gradient(#8db4cf 0%,#a9c3d3 45%,#b79160 70%,#3c4d5e 100%)}
.press{left:700px;top:530px;width:208px;height:220px;background:#fff}
.press-item{position:absolute;left:11px;width:190px}
.thumb{position:absolute;left:0;top:0;width:46px;height:46px}
.press-item .t{position:absolute;left:57px;top:2px;font-size:9px;line-height:13px;color:#333;width:130px}
.press-item .time{position:absolute;left:57px;top:35px}
.finalist{position:absolute;top:797px;width:140px;text-align:center}
.finalist .photo{width:140px;height:140px}
.finalist .nm{margin-top:13px;font-size:10.5px;letter-spacing:.6px;color:#444}
.footer{left:80px;top:1023px;width:1040px;height:219px;background:var(--footer)}
.footer-base{left:80px;top:1242px;width:1040px;height:58px;background:var(--footer-base)}
.f-brand{left:253px;top:1072px;width:140px;text-align:center}
.f-brand .dot{width:40px;height:40px;border-radius:50%;background:#fff;margin:0 auto 10px}
.f-brand .name{font-family:"Ubuntu",sans-serif;font-weight:500;font-size:12px;color:#fff}
.f-col h4{font-weight:400;font-size:12.5px;color:#fff;letter-spacing:.2px;margin-bottom:14px}
.f-col p{font-size:8.5px;line-height:13px;color:#cfcfcf}
.info{display:flex;align-items:center;gap:10px;font-size:8.5px;color:#fff;margin-top:7px}
.info svg{width:14px;flex:none}
.tweet{position:relative;padding-left:26px;margin-bottom:18px}
.tweet i{position:absolute;left:5px;top:2px;width:10px;height:10px;border-radius:50%;background:var(--tw)}
.tweet em{font-style:normal;color:var(--tw)}
.subscribe{display:flex;margin-top:17px}
.subscribe .field{width:103px;height:22px;background:#252525;border:1px solid #333;font-size:8.5px;color:#aaa;line-height:20px;padding-left:9px}
.subscribe .go{width:27px;height:22px;background:var(--tw);color:#fff;font-size:8.5px;text-align:center;line-height:22px}
.copy{left:297px;top:1264px;font-size:8.5px;color:#ccc}
.social{left:840px;top:1262px;display:flex;gap:6px}
.social span{width:18px;height:18px;border-radius:50%;background:#e8e8e8}
.social span:first-child{background:var(--tw)}
</style>
</head>
<body>
<div class="page">
  <div class="abs header"></div>
  <div class="stripe" style="top:0;height:4px"><span class="s1"></span><span class="s2"></span><span class="s3"></span><span class="s4"></span><span class="s5"></span></div>

  <div class="abs brand"><div class="dot"></div><div class="name">MARLOWE TILE FLOOR</div></div>
  <nav class="abs nav"><span>HOME</span><span>FINALISTS</span><span>JURY</span><span>SPONSORS</span><span>ANNOUNCEMENTS</span><span>PRESS</span><span>BLOG</span><span>ABOUT</span><span>CONTACT</span></nav>
  <div class="abs auth">SIGN UP<b>|</b>REGISTER</div>

  <section class="abs hero" role="img" aria-label="Blurred photograph of a warm wooden interior floor"></section>
  <div class="abs badge"><svg width="8" height="8" viewBox="0 0 8 8"><rect x=".5" y="1" width="7" height="6.5" fill="none" stroke="#fff"/><rect x=".5" y="1" width="7" height="2" fill="#fff"/></svg>NOVEMBER 2013</div>
  <h1 class="abs hero-title">1st Annual Marlowe Tile Floor Design Competition</h1>
  <p class="abs hero-text">In January 2014, Marlowe Tile Inc. will launch its 1st Annual Marlowe Tile Floor Design Competition. This design competition will be open to Design and Architecture students of the NYC area. Students and student groups can submit cork flooring design concepts...</p>
  <div class="abs btn">READ MORE</div>

  <div class="abs main"></div>

  <div class="abs sec-title" style="left:298px;top:550px">
    <svg width="14" height="14" viewBox="0 0 14 14"><circle cx="7" cy="7" r="6.5" fill="var(--teal)"/><path d="M4 4c2 0 2 2 4 2s1 3-1 4M9 3c1 1 2 1 2 3" stroke="#fff" stroke-width="1.2" fill="none"/></svg>Announcements</div>
  <div class="abs rule" style="left:295px;top:571px;width:400px"></div>
  <article class="abs card">
    <h3>1st Annual Marlowe Tile Floor Design Competition</h3>
    <div class="time abs" style="left:0;top:67px">3 hours ago</div>
    <p>Lorem Ipsum is simply dummy text of the printing and typesetting industry.. <a href="#">Read more</a></p>
    <div class="abs img-city" role="img" aria-label="Photograph of the New York City skyline over the river"></div>
  </article>

  <aside class="abs press">
    <div class="abs sec-title" style="left:14px;top:20px">
      <svg width="14" height="14" viewBox="0 0 14 14"><circle cx="2.5" cy="11.5" r="1.6" fill="var(--teal)"/><path d="M1 6a7 7 0 0 1 7 7M1 1.5A11.5 11.5 0 0 1 12.5 13" stroke="var(--teal)" stroke-width="2" fill="none"/></svg>Press Release</div>
    <div class="abs rule" style="left:10px;top:41px;width:198px"></div>
    <div class="press-item" style="top:55px"><div class="thumb" role="img" aria-label="City skyscrapers photo" style="background:linear-gradient(#9ab6cc,#6c7a86)"></div><div class="t">A New Yorker doesn't necessarily come from...</div><div class="time">3 minutes ago</div></div>
    <div class="press-item" style="top:113px"><div class="thumb" role="img" aria-label="Portrait photo of a man" style="background:linear-gradient(#d9d4cc,#6e6660)"></div><div class="t">A New Yorker never looks up...</div><div class="time">7 hours ago</div></div>
    <div class="press-item" style="top:171px"><div class="thumb" role="img" aria-label="Photo of colourful cork samples" style="background:linear-gradient(#c98a7a,#e4e0da)"></div><div class="t">A New Yorker doesn't take cabs</div><div class="time">23 hours ago</div></div>
  </aside>

  <div class="abs sec-title" style="left:298px;top:765px">
    <svg width="14" height="14" viewBox="0 0 14 14"><path d="M3 1h8v4a4 4 0 0 1-8 0zM3 2H1v2a2 2 0 0 0 2 2M11 2h2v2a2 2 0 0 1-2 2M6 9h2v2H6zM4 12h6v1.5H4z" fill="var(--teal)" stroke="var(--teal)" stroke-width=".8"/></svg>Finalists</div>
  <div class="abs rule" style="left:295px;top:790px;width:195px"></div>

  <div class="finalist" style="left:296px"><div class="photo" role="img" aria-label="Portrait photo of finalist Aldo Ferrante" style="background:linear-gradient(#e6e6e4,#a59a90)"></div><div class="nm">ALDO FERRANTE, NYC</div></div>
  <div class="finalist" style="left:451px"><div class="photo" role="img" aria-label="Portrait photo of finalist Nadia Brooks" style="background:linear-gradient(#3a2a22,#c99580)"></div><div class="nm">NADIA BROOKS, NYC</div></div>
  <div class="finalist" style="left:607px"><div class="photo" role="img" aria-label="Portrait photo of finalist Theo Marsh" style="background:linear-gradient(#ececea,#c6a58c)"></div><div class="nm">THEO MARSH, NYC</div></div>
  <div class="finalist" style="left:762px"><div class="photo" role="img" aria-label="Portrait photo of finalist Clara Wendt" style="background:linear-gradient(#b8b4b0,#4a3a34)"></div><div class="nm">CLARA WENDT, NYC</div></div>

  <div class="stripe" style="top:1013px;height:10px"><span class="s1"></span><span class="s2"></span><span class="s3"></span><span class="s4"></span><span class="s5"></span></div>
  <footer class="abs footer"></footer>
  <div class="abs f-brand"><div class="dot"></div><div class="name">MARLOWE TILE FLOOR</div></div>

  <div class="abs f-col" style="left:438px;top:1060px;width:140px">
    <h4>CONTACT</h4>
    <p>There are many variations of passages of Lorem Ipsum available, but the majority have suf-</p>
    <div class="info" style="margin-top:12px"><svg viewBox="0 0 14 14" height="14"><path d="M7 1a4 4 0 0 1 4 4c0 3-4 8-4 8S3 8 3 5a4 4 0 0 1 4-4z" fill="var(--tw)"/><circle cx="7" cy="5" r="1.5" fill="#0e0e0e"/></svg>Harbor Lane</div>
    <div class="info"><svg viewBox="0 0 14 10" height="10"><rect width="14" height="10" fill="var(--tw)"/><path d="M0 0l7 5 7-5" stroke="#0e0e0e" fill="none"/></svg>hello@tilevexa.example</div>
    <div class="info"><svg viewBox="0 0 14 14" height="12"><path d="M3 1l3 3-2 2c1 2 2 3 4 4l2-2 3 3-2 2C6 13 1 8 1 3z" fill="var(--tw)"/></svg>555-01420-88300</div>
  </div>

  <div class="abs f-col" style="left:593px;top:1060px;width:160px">
    <h4>LATEST TWEETS</h4>
    <div class="tweet"><i></i><p>Lorem Ipsum is simply dummy text of the printing and typesetting industry. Lorem Ipsum has<br><em>1 Hour Ago</em></p></div>
    <div class="tweet"><i></i><p>Lorem Ipsum is simply dummy text of the printing and typeset-<br><em>1 Hour Ago</em></p></div>
  </div>

  <div class="abs f-col" style="left:763px;top:1060px;width:140px">
    <h4>NEWS LETTER</h4>
    <p>Type your email address below and recive our daily news letter for free</p>
    <div class="subscribe"><div class="field">Email Address</div><div class="go">GO</div></div>
  </div>

  <div class="abs footer-base"></div>
  <div class="abs copy">© 2013 All rights reserved.&nbsp; Marlowe Tile Floor</div>
  <div class="abs social"><span></span><span></span><span></span></div>
</div>
</body>
</html>
```